IT Consulting Site Revamping for Varnel

I've put a skeleton together on my website, but realize I need some help (it's http://pilot.varnel-example.ca).
I've pulled together tidbits from other websites, but really need my site to be cleaned up, and really spruced up.
I primarily focus on the IT needs of small to medium size businesses, taking care of everything from their servers and networks down to their workstations.
I also want a page listing the vendors (and logos) that I work with including Brontisoft, QZWare, Pelvar, Fusk, TQ, ZRL, WUBE, Morva, Trelagate.
There should also be a simple form to get a quote that will email me.
The final design should communicate strength and reliability.
I would like this to be a fully functional website, that I can upload to Plimba Pages, with the same sort of pages that are existing on http://pilot.varnel-example.ca
Updates
Hey everyone,
Hi everyone,
Reason: Hi all,
There are some designers that would like to submit some new designs, so I'm extending the deadline.
Thanks,
Target Market(s)
Small to medium size business owners. This will primarily be males who work in the oil and gas industry.
Industry/Entity Type
Consulting
Look and feel
Each slider illustrates characteristics of the customer's brand and the style your logo design should communicate.

```html
<!DOCTYPE html>
<html lang="en">
<head>
<meta charset="utf-8">
<title>Varnel Solutions</title>
<link href="https://fonts.googleapis.com/css2?family=Ubuntu:wght@400;500;700&display=swap" rel="stylesheet">
<style>
  :root {
    --page-bg: #ececec;
    --brand-blue: #2a78b8;
    --nav-top: #f2f2f2;
    --nav-bottom: #c9c9c9;
    --panel-bg: #c3d3de;
    --card-bg: #e2e2e2;
    --text-dark: #3a3a3a;
    --text-mid: #555555;
    --btn-slate: #6a7f90;
    --btn-green: #3f9a22;
    --btn-orange: #d4501a;
    --btn-brown: #83531a;
    --btn-blue: #2d6a9c;
  }
  * { box-sizing: border-box; margin: 0; padding: 0; }
  html, body { width: 1200px; height: 1079px; overflow: hidden; }
  body {
    background: var(--page-bg);
    font-family: "Ubuntu", sans-serif;
    color: var(--text-dark);
    position: relative;
  }
  .logo {
    position: absolute; left: 163px; top: 34px;
    display: flex; align-items: center; gap: 12px;
  }
  .logo-dot { width: 60px; height: 60px; border-radius: 50%; background: var(--brand-blue); }
  .logo-name { font-size: 38px; font-weight: 500; color: var(--brand-blue); letter-spacing: -0.5px; }

  .main-nav {
    position: absolute; left: 155px; top: 124px; width: 890px; height: 48px;
    background: linear-gradient(var(--nav-top), var(--nav-bottom));
    border-bottom: 3px solid var(--brand-blue);
  }
  .main-nav a {
    position: absolute; top: 14px; transform: translateX(-50%);
    font-size: 15.5px; font-weight: 500; color: var(--brand-blue); text-decoration: none; white-space: nowrap;
  }

  .hero {
    position: absolute; left: 155px; top: 214px; width: 890px; height: 294px;
    background: var(--panel-bg); border-bottom: 3px solid var(--brand-blue);
  }
  .hero-photo {
    position: absolute; left: 0; top: 0; width: 438px; height: 291px;
    background: linear-gradient(120deg, #e9eef5 0%, #9fb3cc 45%, #6f86a6 70%, #c8d4e2 100%);
  }
  .hero-caption {
    position: absolute; left: 0; top: 169px; width: 439px; height: 79px;
    background: rgba(48, 110, 170, 0.82); border-radius: 0 4px 4px 0;
    padding: 15px 16px; color: #fff; font-size: 18.5px; font-weight: 500; line-height: 25px;
  }
  .hero-caption .easy { color: #b6f23a; }
  .hero-caption .affordable { color: #ff9a4a; }
  .hero-caption .reliable { color: #fff27a; }
  .about {
    position: absolute; left: 460px; top: 22px; width: 415px;
  }
  .about h2 { font-size: 15.5px; font-weight: 500; color: var(--text-dark); margin-bottom: 12px; }
  .about h2 span { color: var(--brand-blue); }
  .about p { font-size: 13.6px; line-height: 18.2px; margin-bottom: 18px; }
  .btn {
    display: block; text-align: center; color: #fff; text-decoration: none;
    font-size: 12px; border-radius: 3px; box-shadow: inset 0 1px 0 rgba(255,255,255,.35);
  }
  .about .btn {
    position: absolute; left: -2px; top: 242px; width: 183px; height: 26px; line-height: 26px;
    background: linear-gradient(#4d8fc6, var(--btn-blue)); border: 1px solid #24577f;
  }

  .section-title {
    position: absolute; left: 154px; top: 543px; width: 891px;
    font-size: 17px; font-weight: 400; color: var(--text-dark);
    padding-bottom: 5px; border-bottom: 3px solid var(--brand-blue);
  }

  .service {
    position: absolute; top: 586px; width: 160px; height: 394px;
    background: var(--card-bg); text-align: center;
  }
  .service-photo { width: 160px; height: 159px; }
  .service h3 {
    font-size: 17px; font-weight: 500; color: var(--text-mid); line-height: 22.5px;
    margin-top: 12px; height: 45px; text-transform: uppercase;
  }
  .service p {
    font-size: 13.4px; line-height: 18px; color: var(--text-mid);
    margin: 14px 10px 0; height: 94px;
  }
  .service .btn {
    position: absolute; left: 11px; top: 353px; width: 140px; height: 25px; line-height: 25px;
  }
  .btn-slate { background: linear-gradient(#8ea0ae, var(--btn-slate)); border: 1px solid #52616d; }
  .btn-green { background: linear-gradient(#6cc03e, var(--btn-green)); border: 1px solid #2f7a18; }
  .btn-orange { background: linear-gradient(#f0773a, var(--btn-orange)); border: 1px solid #a83c10; }
  .btn-brown { background: linear-gradient(#a9762d, var(--btn-brown)); border: 1px solid #633d10; }
  .btn-blue { background: linear-gradient(#4d8fc6, var(--btn-blue)); border: 1px solid #24577f; }

  .site-footer {
    position: absolute; left: 155px; top: 1021px; width: 890px; height: 26px;
    background: var(--panel-bg); font-size: 12px; color: var(--text-mid);
    display: flex; justify-content: space-between; align-items: center; padding: 0 10px 0 15px;
  }
</style>
</head>
<body>
  <header class="logo">
    <div class="logo-dot"></div>
    <div class="logo-name">Varnel</div>
  </header>

  <nav class="main-nav">
    <a href="#" style="left:119px">HOME</a>
    <a href="#" style="left:277px">OUR SERVICES</a>
    <a href="#" style="left:435px">ABOUT US</a>
    <a href="#" style="left:592px">OUR PRODUCTS</a>
    <a href="#" style="left:750px">CONTACT US</a>
  </nav>

  <section class="hero">
    <div class="hero-photo" role="img" aria-label="Two IT technicians working in a server room"></div>
    <div class="hero-caption">
      Small Business Information Technology Services<br>
      <span class="easy">Easy,</span> <span class="affordable">Affordable</span> and <span class="reliable">Reliable.</span>
    </div>
    <div class="about">
      <h2>About <span>Varnel Solutions</span></h2>
      <p>Varnel Solutions is a computer solutions provider and IT consulting firm that supports a wide variety of local small businesses in the Calgary area primarily. Our company also provides IT services to businesses throughout Alberta on special projects.</p>
      <p>Varnel has been trusted for over the last 7 years by small business companies like yours. Whether you are looking for an ongoing computer support company, looking to outsource your small business computer work, or just looking for a computer company to help you solve a computer problem, Varnel is your right choice.</p>
      <a class="btn" href="#">read more about us</a>
    </div>
  </section>

  <h2 class="section-title">Our Services</h2>

  <article class="service" style="left:154px">
    <div class="service-photo" role="img" aria-label="Technician kneeling beside server rack cabling" style="background:linear-gradient(160deg,#f4f4f4,#b9bcc2 60%,#7d8690)"></div>
    <h3>Managed IT<br>Services</h3>
    <p>Lorem ipsum dolor sit amet, consectetur adipiscing elit. Nunc vulputate pretium vehicula. Ut a tristique magna.</p>
    <a class="btn btn-slate" href="#">more about it</a>
  </article>

  <article class="service" style="left:337px">
    <div class="service-photo" role="img" aria-label="Close-up of an open hard disk platter" style="background:linear-gradient(150deg,#d9dde3,#3f6fa8 50%,#8a9bb5)"></div>
    <h3>Storage and<br>Virtualization</h3>
    <p>Lorem ipsum dolor sit amet, consectetur adipiscing elit. Nunc vulputate pretium vehicula. Ut a tristique magna.</p>
    <a class="btn btn-green" href="#">more about it</a>
  </article>

  <article class="service" style="left:519px">
    <div class="service-photo" role="img" aria-label="Businessman holding a glowing globe" style="background:linear-gradient(170deg,#5a86c0,#1f3557 55%,#b5a79a)"></div>
    <h3>Networking<br>Services</h3>
    <p>Lorem ipsum dolor sit amet, consectetur adipiscing elit. Nunc vulputate pretium vehicula. Ut a tristique magna.</p>
    <a class="btn btn-orange" href="#">more about it</a>
  </article>

  <article class="service" style="left:702px">
    <div class="service-photo" role="img" aria-label="USB drive and memory card on a disc" style="background:linear-gradient(140deg,#b0582a,#3a2b24 55%,#7d6a8c)"></div>
    <h3>Backup and<br>Recovery</h3>
    <p>Lorem ipsum dolor sit amet, consectetur adipiscing elit. Nunc vulputate pretium vehicula. Ut a tristique magna.</p>
    <a class="btn btn-brown" href="#">more about it</a>
  </article>

  <article class="service" style="left:884px">
    <div class="service-photo" role="img" aria-label="Hard drive with a stethoscope on it" style="background:linear-gradient(150deg,#fafafa,#d6d2a8 55%,#6a6a6a)"></div>
    <h3>Computer<br>Rerpair Services</h3>
    <p>Lorem ipsum dolor sit amet, consectetur adipiscing elit. Nunc vulputate pretium vehicula. Ut a tristique magna.</p>
    <a class="btn btn-blue" href="#">more about it</a>
  </article>

  <footer class="site-footer">
    <span>2012 © Varnel Solutions</span>
    <span>All Rights Reserved</span>
  </footer>
</body>
</html>
```